KMR Business cards

I currently have a logo that was designed by a pixel harbor designer. I would like this to be added to the business card.

We are an innovative new start-up business offering finance solutions to the car dealership market in the UK. So our clients are quiet traditional, so are cards need to fit in, but at the same time show we are a modern online business.

Finance

```html
<!DOCTYPE html>
<html lang="en">
<head>
<meta charset="utf-8">
<title>KMR Business Cards</title>
<link rel="stylesheet" href="https://fonts.googleapis.com/css2?family=Mulish:wght@400;600;700&display=swap">
<style>
  :root {
    --navy: #14193a;
    --navy-deep: #0b0f26;
    --navy-soft: #232a52;
    --white: #ffffff;
    --grey-text: #8a8d99;
    --ink: #1c2147;
    --stage: #e9e9ec;
    --faint: #eef0f3;
  }
  * { box-sizing: border-box; margin: 0; padding: 0; }
  html, body { width: 1200px; height: 784px; overflow: hidden; }
  body {
    background: var(--stage);
    font-family: "Mulish", sans-serif;
    display: flex;
    align-items: center;
    justify-content: center;
    gap: 40px;
  }
  .card {
    position: relative;
    width: 540px;
    height: 309px;
    overflow: hidden;
    box-shadow: 0 6px 20px rgba(0,0,0,0.15);
  }

  /* Front */
  .card-front {
    background: radial-gradient(ellipse at 40% 35%, var(--navy-soft) 0%, var(--navy) 45%, var(--navy-deep) 100%);
    color: var(--white);
  }
  .front-ring {
    position: absolute;
    left: -40px; top: -10px;
    width: 310px; height: 310px;
    border-radius: 50%;
    border: 18px solid rgba(255,255,255,0.05);
  }
  .card-front .brand {
    position: absolute;
    left: 120px; top: 58px;
  }
  .tagline {
    position: absolute;
    left: 0; right: 0; top: 212px;
    text-align: center;
    font-size: 17px;
    letter-spacing: 7px;
    font-weight: 400;
  }

  /* Brand block */
  .brand { display: flex; align-items: center; gap: 14px; }
  .brand-mark {
    width: 84px; height: 84px;
    border-radius: 50%;
    border: 4px solid currentColor;
    flex: none;
  }
  .brand-name {
    font-weight: 600;
    font-size: 26px;
    line-height: 1.05;
  }

  /* Back */
  .card-back { background: var(--white); color: var(--ink); }
  .card-back .brand { position: absolute; left: 42px; top: 38px; }
  .back-ring {
    position: absolute;
    right: -60px; top: 60px;
    width: 200px; height: 200px;
    border-radius: 50%;
    border: 14px solid var(--faint);
  }
  .person { position: absolute; left: 52px; top: 165px; }
  .person-name { font-weight: 700; font-size: 17px; color: var(--ink); }
  .person-role { font-size: 13px; color: var(--grey-text); margin-top: 2px; }
  .contacts {
    position: absolute; left: 52px; top: 210px;
    list-style: none;
    font-size: 12.5px;
    color: var(--ink);
  }
  .contacts li { display: flex; align-items: center; gap: 8px; height: 17px; }
  .contacts svg { width: 13px; height: 13px; flex: none; }
  .back-band {
    position: absolute; left: 0; right: 0; bottom: 0;
    height: 20px;
    background: var(--navy);
  }
</style>
</head>
<body>
  <section class="card card-front">
    <div class="front-ring"></div>
    <div class="brand">
      <div class="brand-mark"></div>
      <div class="brand-name">KMR<br>Kingsway<br>Motor Reserve</div>
    </div>
    <p class="tagline">Drive now, pay later</p>
  </section>

  <section class="card card-back">
    <div class="back-ring"></div>
    <div class="brand">
      <div class="brand-mark"></div>
      <div class="brand-name">KMR<br>Kingsway<br>Motor Reserve</div>
    </div>
    <div class="person">
      <p class="person-name">Daniel Morton</p>
      <p class="person-role">Founder</p>
    </div>
    <ul class="contacts">
      <li>
        <svg viewBox="0 0 16 16" aria-hidden="true"><path d="M4 1l3 3-2 2c1 2 3 4 5 5l2-2 3 3-2 3C7 15 1 9 1 3z" fill="#555"/></svg>
        07700 900415
      </li>
      <li>
        <svg viewBox="0 0 16 16" aria-hidden="true"><circle cx="8" cy="8" r="7" fill="#777"/></svg>
        daniel.morton_kmr
      </li>
      <li>
        <svg viewBox="0 0 16 16" aria-hidden="true"><g fill="none" stroke="#666" stroke-width="1.3"><circle cx="8" cy="8" r="6.5"/><ellipse cx="8" cy="8" rx="3" ry="6.5"/><line x1="1.5" y1="8" x2="14.5" y2="8"/></g></svg>
        www.kingswaymotorreserve.com
      </li>
      <li>
        <svg viewBox="0 0 16 16" aria-hidden="true"><rect x="1" y="3" width="14" height="10" rx="1" fill="#666"/><path d="M1 4l7 5 7-5" fill="none" stroke="#fff" stroke-width="1.2"/></svg>
        daniel.morton@kingswaymotorreserve.com
      </li>
    </ul>
    <div class="back-band"></div>
  </section>
</body>
</html>
```